Business Card Design Project

Roofing Consultant firm needs business card design

R.T. Haverbrook & Co., Inc
Roofing Consultants and Contractors
Specializing in Construction Defect Litigation

4817 Willow Crest Ln.
San Diego, CA 92847
Licences:
CA 514728, AZ 907465, NV 0063512
www.rthaverbrook-example.com

Will need cards for 3 persons:
Robert T. Haverbrook - Principal Consultant
Kevin Sallow - Associate Expert
Marla Vinsett - Controller
ph-555-217-6400
fax -555-217-6402
Cell - (will be 3 different numbers)
Email - (will be 3 different addresses)
Attached graphic is what we had before..the RTH with the roof graphic has been our logo for awhile, but we are open to change.
Updates

I now see we will need to add an email field to the design.  Sorry I didnt think of it when I was setting this up.  Thank you for your submittals. They are all very good. 

Target Market(s)

Attorneys, Homeowner Associations, Insurance Carriers

Industry/Entity Type

Business

Requirements
Must have
• RTH logo roof design. (owner created)

```html
<!DOCTYPE html>
<html lang="en">
<head>
<meta charset="utf-8">
<title>R.T. Haverbrook &amp; Co., Inc — Business Card</title>
<link href="https://fonts.googleapis.com/css2?family=Open+Sans:ital,wdth,wght@0,75..100,300..800;1,75..100,300..800&display=swap" rel="stylesheet">
<style>
  :root{
    --brand-blue:#1f5aa0;
    --deep-blue:#14478a;
    --light-blue:#3f86c9;
    --band-grey:#c3c7cb;
    --ink:#3d3d3d;
    --muted:#5a5a5a;
    --paper:#ffffff;
    --backdrop:#e9ebee;
  }
  *{box-sizing:border-box;margin:0;padding:0}
  html,body{width:1200px;height:960px;overflow:hidden;background:var(--backdrop);font-family:"Open Sans",Arial,sans-serif}
  .canvas{position:relative;width:1200px;height:960px}
  .card{position:absolute;left:250px;width:700px;height:400px;overflow:hidden;box-shadow:0 6px 18px rgba(0,0,0,.18)}
  .card--front{top:60px;background:var(--paper)}
  .card--back{top:500px;background:radial-gradient(ellipse at 65% 35%,var(--light-blue) 0%,var(--brand-blue) 45%,var(--deep-blue) 100%)}
  .waves{position:absolute;inset:0;width:100%;height:100%}

  .brand{position:absolute;left:60px;top:118px}
  .brand__name{display:flex;align-items:center;gap:12px;color:var(--brand-blue);font-weight:600;font-size:22px;line-height:1.2;white-space:nowrap}
  .brand__mark{flex:none;width:18px;height:18px;background:var(--brand-blue)}
  .brand__tagline{margin-top:14px;font-size:12px;font-style:italic;font-weight:700;color:var(--muted)}

  .person{position:absolute;right:40px;top:40px;text-align:right;font-stretch:75%}
  .person__name{font-weight:600;font-size:24px;line-height:1.2;color:var(--ink)}
  .person__title{font-weight:400;font-size:16px;line-height:1.3;color:var(--ink)}

  .contact{position:absolute;right:40px;top:118px;list-style:none;text-align:right}
  .contact li{display:flex;justify-content:flex-end;align-items:center;gap:8px;font-stretch:75%;font-weight:400;font-size:15px;color:var(--ink);line-height:20px;white-space:nowrap}
  .contact svg{flex:none;width:11px;height:11px;fill:var(--ink)}

  .licences{position:absolute;left:60px;bottom:32px;color:#fff;font-style:italic;font-size:13px}

  .back-brand{position:absolute;right:70px;bottom:95px;display:flex;align-items:center;gap:12px;color:#fff;font-weight:600;font-size:28px;white-space:nowrap}
  .back-brand__mark{width:20px;height:20px;background:#fff}
</style>
</head>
<body>
<main class="canvas">
  <section class="card card--front" aria-label="Card front">
    <svg class="waves" viewBox="0 0 700 400" preserveAspectRatio="none" aria-hidden="true">
      <path d="M0 258 C160 250 300 300 450 292 S640 270 700 262 L700 400 L0 400Z" fill="var(--band-grey)"/>
      <path d="M0 272 C160 264 300 312 450 304 S640 284 700 278 L700 400 L0 400Z" fill="#fff"/>
      <path d="M0 280 C160 272 300 320 450 312 S640 292 700 286 L700 400 L0 400Z" fill="var(--brand-blue)"/>
    </svg>
    <div class="brand">
      <p class="brand__name"><span class="brand__mark"></span>R.T. Haverbrook &amp; Co., Inc</p>
      <p class="brand__tagline">Roofing Consultants and Contractors</p>
    </div>
    <div class="person">
      <h1 class="person__name">Robert T. Haverbrook</h1>
      <p class="person__title">Principal Consultant</p>
    </div>
    <ul class="contact">
      <li>4817 Willow Crest Ln., San Diego, CA 92847 <svg viewBox="0 0 12 12"><path d="M6 1 0 6h2v5h3V8h2v3h3V6h2z"/></svg></li>
      <li>555-217-6400 <svg viewBox="0 0 12 12"><path d="M2 1h3l1 3-2 1a7 7 0 0 0 3 3l1-2 3 1v3c-6 1-10-4-9-9z"/></svg></li>
      <li>555-217-6402 <svg viewBox="0 0 12 12"><path d="M3 1h6v3H3zM1 5h10v5H9v1H3v-1H1z"/></svg></li>
      <li>555-217-6419 <svg viewBox="0 0 12 12"><path d="M3 0h6v12H3zM4 1v9h4V1z" fill-rule="evenodd"/></svg></li>
      <li>robert@rthaverbrook-example.com <svg viewBox="0 0 12 12"><path d="M0 2h12v8H0zM1 3l5 4 5-4v-.5H1z" fill-rule="evenodd"/></svg></li>
      <li>www.rthaverbrook-example.com <svg viewBox="0 0 12 12"><circle cx="6" cy="6" r="5.5"/></svg></li>
    </ul>
    <p class="licences">Licences: CA #514728 AZ #907465 NV #0063512</p>
  </section>

  <section class="card card--back" aria-label="Card back">
    <p class="back-brand"><span class="back-brand__mark"></span>R.T. Haverbrook &amp; Co., Inc</p>
  </section>
</main>
</body>
</html>
```